Business Cards & Stationary Levy Appeal Counsel Partners
Business Cards & Stationary
Business Cards & Stationary Levy Appeal Counsel Partners  - Law
Creative Brief
Professional
Nora Bastable
Attorney
27480 Heron Bluff Boulevard, #200 Leawood, Kansas 66389
Nbastable@lacp-mail.net
LACP-mail.net
The card will need to have our logo on it and the tag line: Member, National Assessment Dispute Alliance

```html
<!DOCTYPE html>
<html lang="en">
<head>
<meta charset="utf-8">
<title>Levy Appeal Counsel Partners — Stationery Set</title>
<link href="https://fonts.googleapis.com/css2?family=Cinzel:wght@500&family=Open+Sans:wght@400;600&display=swap" rel="stylesheet">
<style>
:root{
  --stage:#3b3b3d;
  --paper:#ffffff;
  --paper-shade:#eceef2;
  --navy:#0f1f47;
  --blue:#1f4fa0;
  --sky:#6d93d6;
  --ink:#2b2f3a;
  --muted:#8a8f9a;
  --silver:#c9ccd2;
  --caption:#cfd2d8;
}
*{margin:0;padding:0;box-sizing:border-box}
html,body{width:1200px;height:343px;overflow:hidden;background:var(--stage);font-family:"Open Sans",sans-serif}
.set{position:relative;width:1200px;height:343px}
.sheet{position:absolute;background:var(--paper);overflow:hidden;box-shadow:0 2px 6px rgba(0,0,0,.45)}
.swoosh{position:absolute;left:0;bottom:0;width:100%;display:block}
.brand{font-family:"Cinzel",serif;font-weight:500;color:var(--navy);line-height:1.15;white-space:nowrap}
.brand .dot{display:inline-block;width:.6em;height:.6em;background:var(--blue);margin-right:.35em;vertical-align:middle}
.watermark{position:absolute;left:0;width:100%;font-family:"Cinzel",serif;font-weight:500;color:var(--silver);opacity:.55;text-align:center;line-height:1.1}
.tiny{font-size:5px;color:var(--muted);line-height:1.45;white-space:nowrap}

/* hero brand */
.brand-hero{position:absolute;left:18px;top:14px;width:150px;color:#fff;font-family:"Cinzel",serif;font-weight:500;font-size:15px;line-height:1.15}
.brand-hero .dot{display:inline-block;width:10px;height:10px;background:#fff;margin-right:6px;vertical-align:middle}

/* business card */
.card{left:24px;top:149px;width:136px;height:115px}
.card .brand{position:absolute;top:9px;left:9px;font-size:6px}
.card .name{position:absolute;left:9px;top:34px;font-size:7px;font-weight:600;color:var(--ink)}
.card .role{position:absolute;left:9px;top:44px;font-size:5px;color:var(--blue)}
.card .contact{position:absolute;left:9px;top:54px}
.card-caption{position:absolute;left:24px;top:271px;width:160px;font-size:5px;color:var(--caption);white-space:nowrap}

/* letterheads */
.letter{top:19px;width:158px;height:305px}
.letter-a{left:226px}
.letter-b{left:403px}
.letter .brand{position:absolute;top:9px;left:0;width:100%;font-size:6.5px;text-align:center}
.letter .watermark{top:128px;font-size:12px}
.letter .footer{position:absolute;bottom:6px;width:100%;text-align:center;font-size:4px;color:#e4e9f5}

/* envelopes */
.env{left:636px;width:221px}
.env-a{top:96px;height:106px}
.env-b{top:210px;height:102px}
.env .brand{position:absolute;left:8px;top:8px;font-size:5.5px}

/* stacked envelope backs */
.flapped{height:82px}
.flapped svg.flap{position:absolute;left:0;top:0;width:100%;height:100%}
.flapped.one{top:7px;left:907px;width:269px;background:var(--paper-shade)}
.flapped.one .brand{position:absolute;left:0;top:8px;width:100%;font-size:5.5px;text-align:center;color:#fff}
.flapped.two{top:127px;left:907px;width:269px;height:101px}
.flapped.three{top:236px;left:907px;width:269px;height:78px}
</style>
</head>
<body>
<main class="set">

  <div class="brand-hero"><span class="dot"></span>Levy Appeal Counsel Partners</div>

  <section class="sheet card" aria-label="Business card">
    <div class="brand"><span class="dot"></span>Levy Appeal Counsel Partners</div>
    <p class="name">Nora Bastable</p>
    <p class="role">Attorney</p>
    <div class="contact tiny">
      <p>27480 Heron Bluff Boulevard, #200</p>
      <p>Leawood, Kansas 66389</p>
      <p>Nbastable@lacp-mail.net</p>
      <p>LACP-mail.net</p>
    </div>
    <svg class="swoosh" viewBox="0 0 136 22" height="22" preserveAspectRatio="none">
      <path d="M0 12 Q68 2 136 9 L136 22 L0 22Z" fill="var(--navy)"/>
      <path d="M0 10 Q68 0 136 7" stroke="var(--sky)" stroke-width="1" fill="none"/>
    </svg>
  </section>
  <p class="card-caption">Member, National Assessment Dispute Alliance</p>

  <section class="sheet letter letter-a" aria-label="Letterhead">
    <div class="brand"><span class="dot"></span>Levy Appeal Counsel Partners</div>
    <div class="watermark">Levy Appeal<br>Counsel Partners</div>
    <svg class="swoosh" viewBox="0 0 158 40" height="40" preserveAspectRatio="none">
      <path d="M0 10 Q79 30 158 14 L158 40 L0 40Z" fill="var(--navy)"/>
      <path d="M0 8 Q79 28 158 12" stroke="var(--sky)" stroke-width="1.5" fill="none"/>
    </svg>
    <p class="footer">LACP-mail.net</p>
  </section>

  <section class="sheet letter letter-b" aria-label="Second page letterhead">
    <div class="brand"><span class="dot"></span>Levy Appeal Counsel Partners</div>
    <div class="watermark">Levy Appeal<br>Counsel Partners</div>
    <svg class="swoosh" viewBox="0 0 158 40" height="40" preserveAspectRatio="none">
      <path d="M0 10 Q79 30 158 14 L158 40 L0 40Z" fill="var(--navy)"/>
      <path d="M0 8 Q79 28 158 12" stroke="var(--sky)" stroke-width="1.5" fill="none"/>
    </svg>
    <p class="footer">LACP-mail.net</p>
  </section>

  <section class="sheet env env-a" aria-label="Envelope">
    <div class="brand"><span class="dot"></span>Levy Appeal Counsel Partners</div>
    <svg class="swoosh" viewBox="0 0 221 28" height="28" preserveAspectRatio="none">
      <path d="M0 6 Q110 26 221 4 L221 28 L0 28Z" fill="var(--navy)"/>
      <path d="M0 4 Q110 24 221 2" stroke="var(--sky)" stroke-width="1.5" fill="none"/>
    </svg>
  </section>

  <section class="sheet env env-b" aria-label="Return envelope">
    <div class="brand"><span class="dot"></span>Levy Appeal Counsel Partners</div>
    <svg class="swoosh" viewBox="0 0 221 24" height="24" preserveAspectRatio="none">
      <path d="M0 6 Q110 22 221 4 L221 24 L0 24Z" fill="var(--navy)"/>
      <path d="M0 4 Q110 20 221 2" stroke="var(--sky)" stroke-width="1.5" fill="none"/>
    </svg>
  </section>

  <section class="sheet flapped one" aria-label="Envelope back with navy flap">
    <svg class="flap" viewBox="0 0 269 82" preserveAspectRatio="none">
      <path d="M0 0 L269 0 L269 14 Q134 58 0 14Z" fill="var(--navy)"/>
      <path d="M0 14 Q134 58 269 14" stroke="var(--sky)" stroke-width="1.5" fill="none"/>
    </svg>
    <div class="brand">Levy Appeal Counsel Partners</div>
  </section>

  <section class="sheet flapped two" aria-label="Envelope back">
    <svg class="flap" viewBox="0 0 269 101" preserveAspectRatio="none">
      <path d="M0 0 L269 0 L269 10 Q134 50 0 10Z" fill="var(--navy)"/>
      <path d="M0 10 L134 64 L269 10" stroke="var(--silver)" stroke-width="1" fill="none"/>
    </svg>
  </section>

  <section class="sheet flapped three" aria-label="Envelope back, plain">
    <svg class="flap" viewBox="0 0 269 78" preserveAspectRatio="none">
      <path d="M0 0 L134 44 L269 0" stroke="var(--silver)" stroke-width="1" fill="none"/>
      <path d="M0 78 L104 36 M269 78 L165 36" stroke="var(--silver)" stroke-width="1" fill="none"/>
    </svg>
  </section>

</main>
</body>
</html>
```